Silver Fern Apothecary needs a label design or modification for new Kratom Co., need simple, eye catch

New company in Northern California that is going wholesale and retail for Kratom, a natural alternative from todays pharmaceutical drugs, we want to provide a better quality product than what the public in our area is generally exposed to, and eventually wider than Northern California

We need a better, eye catching, simple label design for our new Kratom line at Silver Fern Apothecary
This line will be Kratom that is harvested from the "Wild"....or "Forest Grown"
attached are files for capsule bottles, would like to be similar, but i don't feel the label "pops" or will grab enough attention.
It will be for Kratom ultra fine powder of premium grade, no stems and veins or any other additives or fillers

The existing Logo was created by pixel forge and would like it to be used
maybe with a graphic drawing of a Kratom leaf in the background ? not sure.
We are open to new ideas.

Maybe the label needs to be totally different, not sure.
Saw a friends project from pixel forge for Kratom, it was simple and i loved it, maybe even reduce the number of colors, maybe not
need the files in "AI" and would be nice if layered
there will be two different sizes
100g (3.527 oz) needs to be in the lower third of the bottom, in an area of
4 1/2" x 6"
50g (1.764 oz) in an area of 3 3/8" x 4"
The number declarations need to be at least 3/16" tall
as you will see from the attached files, some have green, red or white colors on the top and bottom of the label, this is to help the eye better catch the general type of strain for the customer and for the people selling the product
all other needed info will be in the attached files

The attached files are for Tortoise Kratom Tablets, the newer product is for Summit Kratom Blend (or maybe Select Kratom Blend), of various types.
Our product is better than most others and usually much stronger.
We provide consistency of product quality, which is hard to find with this item.

When printed "Silver Fern" doesnt stand out, especially with a black background, the black may make the printing of the gold darker than what it should be. Not sure if "Silver Fern" would be appropriate in white, or if i need a new design.

The Type of each kind may be added later simply because we carry so many different kinds, and as is said, we are open to new ideas.
Thank You

Target Market(s)

General public through wholesale to retailers, Kratom community

Industry/Entity Type

It Company

Font styles to use
Sans Serif
Other font styles liked:
• segoe print

Colors
fece3e
abd036
ec1f27
ffffff

Requirements
Must have
• size declarations of at least 3/16"
• and be taller than wide
Nice to have
• graphic picture of a Kratom leaf
Should not have
• for human consumption

```html
<!DOCTYPE html>
<html lang="en">
<head>
<meta charset="utf-8">
<title>Silver Fern Apothecary – Select Kratom Blend Label</title>
<link href="https://fonts.googleapis.com/css2?family=Montserrat:wght@700&family=Oswald:wght@500;600&display=swap" rel="stylesheet">
<style>
  :root {
    --stage: #e6e6e6;
    --label: #ffffff;
    --red: #ec1f27;
    --red-deep: #c4161d;
    --green: #1f9a3f;
    --green-soft: #abd036;
    --gold: #b88a2e;
    --gold-light: #d9b25a;
    --powder: #6aa32e;
    --bowl: #9a6a3c;
    --claim-icon: #555555;
  }
  * { box-sizing: border-box; margin: 0; padding: 0; }
  html, body { width: 1200px; height: 662px; overflow: hidden; }
  body {
    background: var(--stage);
    display: flex; align-items: center; justify-content: center;
  }
  .label {
    position: relative;
    width: 466px; height: 620px;
    background: var(--label);
    overflow: hidden;
    box-shadow: 0 6px 24px rgba(0,0,0,.12);
  }
  .band { position: absolute; left: 0; right: 0; height: 40px; }
  .band--top { top: 0; background: linear-gradient(to bottom, var(--red) 0 7px, rgba(236,31,39,.3) 7px, rgba(236,31,39,0)); }
  .band--bottom { bottom: 0; background: linear-gradient(to top, var(--red) 0 9px, rgba(236,31,39,.3) 9px, rgba(236,31,39,0)); }

  .emblem { position: absolute; left: 0; top: 0; width: 466px; height: 480px; }

  .brand {
    position: absolute; left: 0; right: 0; top: 214px;
    text-align: center;
    font-family: "Montserrat", sans-serif; font-weight: 700;
    color: var(--green);
    line-height: 1;
  }
  .brand__name { font-size: 40px; letter-spacing: 1px; }
  .brand__sub { font-size: 24px; letter-spacing: 1px; margin-top: 12px; }

  .badge {
    position: absolute; left: 352px; top: 318px;
    width: 60px; height: 60px; border-radius: 50%;
    border: 3px solid var(--green);
  }

  .product {
    position: absolute; left: 0; right: 0; top: 366px;
    text-align: center;
    font-family: "Oswald", sans-serif; font-weight: 600;
    line-height: 1;
  }
  .product__grade { color: var(--gold); font-size: 32px; }
  .product__name { color: var(--green); font-size: 42px; margin-top: 4px; }

  .claims {
    position: absolute; left: 0; right: 0; top: 458px;
    display: flex; justify-content: center; gap: 18px;
    font-family: "Oswald", sans-serif; font-weight: 500; font-size: 13px;
    color: var(--red);
  }
  .claim { display: flex; align-items: center; gap: 6px; }
  .claim__dot { width: 13px; height: 13px; border-radius: 50%; border: 1.5px solid var(--claim-icon); }

  .serving-photo {
    position: absolute; left: 132px; top: 484px; width: 210px; height: 106px;
    border-radius: 14px;
    background: linear-gradient(to bottom, var(--powder) 0%, #7f9a3a 55%, var(--bowl) 100%);
  }
  .net-weight {
    position: absolute; left: 50%; bottom: 3px; transform: translateX(-50%);
    background: var(--red-deep); color: #fff;
    font-family: "Oswald", sans-serif; font-weight: 600; font-size: 15px;
    padding: 4px 18px; border-radius: 12px 12px 0 0;
    white-space: nowrap;
  }
</style>
</head>
<body>
  <main class="label">
    <div class="band band--top"></div>
    <div class="band band--bottom"></div>

    <svg class="emblem" viewBox="0 0 466 480" aria-hidden="true">
      <circle cx="245" cy="230" r="128" fill="none" stroke="var(--green)" stroke-width="3" opacity=".85"/>
      <circle cx="232" cy="138" r="58" fill="var(--gold-light)"/>
      <polygon points="140,62 160,96 120,96" fill="var(--green-soft)" opacity=".45"/>
      <polygon points="68,232 80,252 56,252" fill="var(--green-soft)" opacity=".45"/>
      <polygon points="392,150 406,174 378,174" fill="var(--green-soft)" opacity=".35"/>
      <polygon points="158,348 170,368 146,368" fill="var(--green-soft)" opacity=".45"/>
    </svg>

    <div class="brand">
      <div class="brand__name">SILVER FERN</div>
      <div class="brand__sub">APOTHECARY</div>
    </div>

    <div class="badge"></div>

    <div class="product">
      <div class="product__grade">SELECT</div>
      <div class="product__name">KRATOM BLEND</div>
    </div>

    <div class="claims">
      <span class="claim"><span class="claim__dot"></span>NO ADDITIVES</span>
      <span class="claim"><span class="claim__dot"></span>NO FILLERS</span>
    </div>

    <div class="serving-photo" role="img" aria-label="Photo of a wooden bowl of green kratom powder with a spoon and fresh leaves"></div>

    <div class="net-weight">100G (3.527 OZ)</div>
  </main>
</body>
</html>
```